Anzeigengestaltung für Fitnesscenter
Zielgruppe
24/7 Fitnesscenter
Geschenk für Weihnachten
Aufgabenstellung
Anzeige oder flyer bzw. Post für Instagram für ein Weihnachtsgeschenk:
- Weihnachtsgeschenk? Schenke Sie ein Jahr Fitness in unserem 24/7 Fitnessstudio in Götzis
- EUR 239,-- Jahresmitgliedschaft
- Keine Zustazkosten
hantelZeit 24/7 im Business Hotel Quellbrunn in Götzis
Tel. 00430000123456 mail: lukas@wohn-beratung.example
Sie können den Text gerne so ändern wie sie möchten, bitte das ganze eher schwarz weiss gehalten-- danke

```html
<!DOCTYPE html>
<html lang="de">
<head>
<meta charset="utf-8">
<title>hantelZeit 24/7 – Neues Jahr, neue Form</title>
<link rel="stylesheet" href="https://fonts.googleapis.com/css2?family=Rubik+Dirt&family=Titan+One&family=Montserrat:ital,wght@1,400;1,500&display=swap">
<style>
:root{
  --stage:#f5f5f5;
  --ink:#000;
  --paper:#fff;
  --green:#1e9a2c;
  --photo-dark:#1b1b1b;
  --photo-mid:#4a3a30;
  --gym-floor:#a98a68;
  --gym-wall:#d9d9d9;
}
*{margin:0;padding:0;box-sizing:border-box}
html,body{width:1200px;height:960px;overflow:hidden;background:var(--stage)}
.ad{position:absolute;top:39px;width:496px;background:var(--ink);overflow:hidden;color:var(--paper)}
.ad--square{left:96px;height:606px}
.ad--portrait{left:607px;height:881px}
.band{position:absolute;left:0;top:0;width:100%;height:100%}
.athlete{position:absolute;background:radial-gradient(ellipse at 50% 30%,var(--photo-mid),var(--photo-dark) 70%);border-radius:40% 40% 10% 10%}
.headline{position:absolute;font-family:"Rubik Dirt",system-ui,sans-serif;font-weight:400;line-height:1.08;transform:rotate(-3deg);transform-origin:left top;white-space:nowrap;z-index:3}
.offer{position:absolute;font-family:"Titan One",system-ui,sans-serif;text-transform:uppercase;letter-spacing:.04em;line-height:1.12;transform:rotate(-3deg);transform-origin:left top;z-index:3}
.price{font-size:40px;letter-spacing:.01em;line-height:1}
.membership{font-size:15px}
.rule{height:2px;background:var(--paper);margin:10px 0 12px}
.gym-photo{position:absolute;border:5px solid var(--paper);background:linear-gradient(180deg,var(--photo-dark) 0%,var(--gym-wall) 40%,var(--gym-floor) 100%);z-index:2}
.brand{position:absolute;font-family:"Titan One",system-ui,sans-serif;font-size:32px;line-height:1;color:var(--paper);z-index:3}
.contact{position:absolute;font-family:"Montserrat",system-ui,sans-serif;font-style:italic;font-size:12.5px;line-height:1.4;z-index:3}
.contact p{display:flex;align-items:center;gap:6px}
.contact .address{margin-bottom:10px}
.contact svg{width:11px;height:11px;flex:none}
.footer-band{position:absolute;left:0;width:100%;background:var(--green)}
</style>
</head>
<body>

<section class="ad ad--square">
  <svg class="band" viewBox="0 0 496 606" preserveAspectRatio="none" aria-hidden="true">
    <defs>
      <linearGradient id="greenSq" x1="0" y1="0" x2="0" y2="1">
        <stop offset="0" stop-color="#23a532"/>
        <stop offset="1" stop-color="#137a20"/>
      </linearGradient>
    </defs>
    <polygon fill="url(#greenSq)" points="0,206 60,198 140,188 220,180 300,176 400,170 496,167 496,362 420,368 320,380 220,388 120,392 0,397"/>
  </svg>
  <div class="athlete" role="img" aria-label="Foto: muskulöser Mann im schwarzen Tanktop beim Bizepscurl mit Kurzhantel" style="left:166px;top:120px;width:168px;height:315px"></div>

  <h1 class="headline" style="left:54px;top:38px;font-size:48px">NEUES JAHR<br>NEUE FORM</h1>

  <p class="offer" style="left:29px;top:236px;font-size:18px">Schenke Sie<br>ein Jahr<br>Fitness in<br>unserem 24/7<br>Fitnessstudio<br>in Götzis</p>

  <div class="offer" style="left:346px;top:200px;width:140px">
    <div class="price">239€</div>
    <div class="membership" style="margin-top:8px">Jahresmit-<br>gliedschaft</div>
    <div class="rule"></div>
    <div class="membership">Keine Zustaz-<br>kosten</div>
  </div>

  <div class="gym-photo" role="img" aria-label="Foto: Trainingsbereich mit grünem Rack und Geräten" style="left:302px;top:368px;width:210px;height:128px;transform:rotate(-3deg)"></div>
  <div class="gym-photo" role="img" aria-label="Foto: Gerätebereich mit Holzboden" style="left:281px;top:478px;width:210px;height:140px;transform:rotate(-3deg)"></div>

  <div class="footer-band" style="top:584px;height:22px"></div>

  <div class="brand" style="left:40px;top:440px">hantelZeit</div>
  <div class="contact" style="left:40px;top:484px">
    <p class="address">hantelZeit 24/7 im Business<br>Hotel Quellbrunn in Götzis</p>
    <p><svg viewBox="0 0 24 24"><path fill="#1e9a2c" d="M6.6 10.8a15 15 0 0 0 6.6 6.6l2.2-2.2a1 1 0 0 1 1-.25 11 11 0 0 0 3.6.6 1 1 0 0 1 1 1V20a1 1 0 0 1-1 1A17 17 0 0 1 3 4a1 1 0 0 1 1-1h3.5a1 1 0 0 1 1 1c0 1.25.2 2.45.6 3.6a1 1 0 0 1-.25 1z"/></svg>00430000123456</p>
    <p><svg viewBox="0 0 24 24"><path fill="#1e9a2c" d="M2 5h20v14H2zm2 2v.5l8 5 8-5V7l-8 5z"/></svg>lukas@wohn-beratung.example</p>
  </div>
</section>

<section class="ad ad--portrait">
  <svg class="band" viewBox="0 0 496 881" preserveAspectRatio="none" aria-hidden="true">
    <defs>
      <linearGradient id="greenPt" x1="0" y1="0" x2="0" y2="1">
        <stop offset="0" stop-color="#23a532"/>
        <stop offset=".55" stop-color="#137a20"/>
        <stop offset="1" stop-color="#000"/>
      </linearGradient>
    </defs>
    <polygon fill="url(#greenPt)" points="0,317 80,308 180,296 280,286 380,278 496,273 496,601 0,601"/>
  </svg>
  <div class="athlete" role="img" aria-label="Foto: muskulöser Mann im schwarzen Tanktop beim Bizepscurl mit Kurzhantel" style="left:261px;top:172px;width:200px;height:362px"></div>

  <h1 class="headline" style="left:36px;top:80px;font-size:62px">NEUES JAHR<br>NEUE FORM</h1>

  <p class="offer" style="left:33px;top:350px;font-size:18px">Schenke Sie ein<br>Jahr Fitness in<br>unserem 24/7<br>Fitnessstudio in<br>Götzis</p>

  <div class="offer" style="left:36px;top:486px;width:230px">
    <div style="display:flex;align-items:center;gap:10px">
      <span class="price">239€</span>
      <span class="membership">Jahresmit-<br>gliedschaft</span>
    </div>
    <div class="rule"></div>
    <div class="membership" style="font-size:16px">Keine Zustazkosten</div>
  </div>

  <div class="gym-photo" role="img" aria-label="Foto: Trainingsbereich mit grünem Rack und Geräten" style="left:269px;top:532px;width:240px;height:158px;transform:rotate(-3deg)"></div>
  <div class="gym-photo" role="img" aria-label="Foto: Gerätebereich mit Holzboden" style="left:261px;top:690px;width:245px;height:162px;transform:rotate(-3deg)"></div>

  <div class="footer-band" style="top:848px;height:33px"></div>

  <div class="brand" style="left:36px;top:654px">hantelZeit</div>
  <div class="contact" style="left:36px;top:698px">
    <p class="address">hantelZeit 24/7 im Business<br>Hotel Quellbrunn in Götzis</p>
    <p><svg viewBox="0 0 24 24"><path fill="#1e9a2c" d="M6.6 10.8a15 15 0 0 0 6.6 6.6l2.2-2.2a1 1 0 0 1 1-.25 11 11 0 0 0 3.6.6 1 1 0 0 1 1 1V20a1 1 0 0 1-1 1A17 17 0 0 1 3 4a1 1 0 0 1 1-1h3.5a1 1 0 0 1 1 1c0 1.25.2 2.45.6 3.6a1 1 0 0 1-.25 1z"/></svg>00430000123456</p>
    <p><svg viewBox="0 0 24 24"><path fill="#1e9a2c" d="M2 5h20v14H2zm2 2v.5l8 5 8-5V7l-8 5z"/></svg>lukas@wohn-beratung.example</p>
  </div>
</section>

</body>
</html>
```